Business Card and letterhead Design for The Yield Lantern

we now have a logo designed on gigmarket (thanks), now we would like to use this logo to create a business card (that we can use for printing and that we can edit easily) we would like lots of options and a letterhead template (in word)
the name for the sample card is: Neville [login to view URL]
job title: Director.
address:
L14, Quay Wing,
Wattle Court,
58 Merrow St,
Sydney,
NSW 2000

```html
<!DOCTYPE html>
<html lang="en">
<head>
<meta charset="utf-8">
<title>The Yield Lantern – Stationery</title>
<link rel="stylesheet" href="https://fonts.googleapis.com/css2?family=Oswald:wght@400;500;600&display=swap">
<style>
  :root {
    --red: #e0121c;
    --red-deep: #b30c17;
    --white: #ffffff;
    --paper-bg: #ece7e1;
    --soft-mark: #f3ecea;
  }
  * { margin: 0; padding: 0; box-sizing: border-box; }
  html, body { width: 1200px; height: 809px; overflow: hidden; }
  body {
    background: var(--paper-bg);
    font-family: "Oswald", sans-serif;
    position: relative;
  }
  .card {
    position: absolute;
    width: 360px;
    height: 206px;
    border-radius: 12px;
    background: linear-gradient(135deg, var(--red) 0%, var(--red-deep) 100%);
    color: var(--white);
    overflow: hidden;
  }
  .card-front { left: 120px; top: 150px; }
  .card-back { left: 120px; top: 430px; }

  .brand-name {
    font-family: "Oswald", sans-serif;
    font-weight: 600;
    color: var(--white);
    white-space: nowrap;
    display: flex;
    align-items: center;
    gap: 10px;
  }
  .brand-dot {
    width: 30px; height: 30px;
    border-radius: 50%;
    background: var(--white);
    flex: none;
  }
  .card-front .brand-name {
    position: absolute;
    left: 42px; top: 78px;
    font-size: 34px;
  }

  .card-back .contact-name {
    position: absolute; left: 22px; top: 28px;
    font-size: 19px; font-weight: 500; letter-spacing: 0.5px;
    text-transform: uppercase;
  }
  .card-back .contact-role {
    position: absolute; left: 22px; top: 54px;
    font-size: 9px; letter-spacing: 1px; text-transform: uppercase;
  }
  .card-back .address {
    position: absolute; left: 22px; top: 110px;
    font-size: 9.5px; line-height: 14px; text-transform: uppercase;
  }
  .contact-line { display: flex; align-items: center; gap: 6px; }
  .contact-line svg { width: 9px; height: 9px; flex: none; }
  .card-back .brand-square {
    position: absolute; right: 40px; top: 40px;
    width: 74px; height: 74px;
    background: var(--white);
    opacity: 0.9;
  }

  .letterhead {
    position: absolute;
    left: 610px; top: 36px;
    width: 520px; height: 737px;
    overflow: hidden;
    background: linear-gradient(135deg, var(--red) 0%, var(--red-deep) 100%);
  }
  .letterhead-sheet { position: absolute; inset: 0; }
  .letterhead .brand-name {
    position: absolute; left: 30px; top: 22px;
    font-size: 24px;
  }
  .letterhead .brand-dot { width: 22px; height: 22px; }
  .letterhead-footer {
    position: absolute; right: 22px; bottom: 20px;
    text-align: right; color: var(--white);
    font-size: 12.5px; line-height: 17px; letter-spacing: 0.5px;
    text-transform: uppercase;
  }
  .letterhead-note {
    position: absolute; left: 20px; bottom: 22px;
    color: var(--white); font-size: 6px; line-height: 8px;
    text-transform: uppercase; opacity: 0.85;
  }
</style>
</head>
<body>

  <section class="card card-front" aria-label="Business card front">
    <div class="brand-name"><span class="brand-dot"></span>The Yield Lantern</div>
  </section>

  <section class="card card-back" aria-label="Business card back">
    <div class="contact-name">Neville A. Harrow</div>
    <div class="contact-role">Director</div>
    <div class="brand-square"></div>
    <div class="address">
      <div>L14 Quay Wing</div>
      <div>Wattle Court, 58 Merrow St, Sydney NSW 2000</div>
      <div class="contact-line">
        <svg viewBox="0 0 10 10"><path d="M2 0.5 L4 2.5 L3 3.8 Q4.3 5.8 6.2 7 L7.5 6 L9.5 8 L8 9.5 Q3.5 9 0.5 2 Z" fill="#fff"/></svg>
        (02)5550-1834
      </div>
      <div class="contact-line">
        <svg viewBox="0 0 10 10"><rect x="0.5" y="2" width="9" height="6.5" fill="#fff"/><path d="M0.5 2 L5 5.5 L9.5 2" stroke="#c10f19" stroke-width="0.8" fill="none"/></svg>
        hello@yieldlantern.com
      </div>
      <div class="contact-line">
        <svg viewBox="0 0 10 10"><circle cx="5" cy="5" r="4.5" fill="#fff"/></svg>
        www.yieldlantern.com
      </div>
    </div>
  </section>

  <section class="letterhead" aria-label="Letterhead">
    <svg class="letterhead-sheet" viewBox="0 0 520 737" width="520" height="737">
      <ellipse cx="260" cy="380" rx="345" ry="318" fill="#ffffff"/>
      <circle cx="260" cy="385" r="120" fill="#f6eeec"/>
    </svg>
    <div class="brand-name"><span class="brand-dot"></span>The Yield Lantern</div>
    <div class="letterhead-note">
      <div>Registered office</div>
      <div>58 Merrow St Sydney</div>
    </div>
    <div class="letterhead-footer">
      <div>(02)5550-1834</div>
      <div>hello@yieldlantern.com</div>
      <div>www.yieldlantern.com</div>
    </div>
  </section>

</body>
</html>
```